Design a Website for an IT Support Company

We are an IT support company that provides commercial IT support and services to small and medium sized businesses. We are in need of a website to be developed for our business.
We would like to work with someone who is either familiar with the IT field, or has developed a website for an IT support company in the past.
Some examples of designs/layouts that we like:
https://www.velmorask.example/
http://www.quibenstack.example/
http://572zo.example/
http://www.guspelnetworks.example/
http://www.ourba.example/
I have attached a word document that gives a menu system/page layout format that we would like for our website as well as branch office phone numbers. Our logo is also attached that you can use for your design purposes. We currently do not have copy produced for all of the pages outlined in the word document, but would get this done during the project with the selected designer.
We would like the website to be SEO friendly & fully responsive. We would prefer a Wordpress format, however, we are open to HTML formats as well.

```html
<!DOCTYPE html>
<html lang="en">
<head>
<meta charset="utf-8">
<title>Korvane IT – IT Support for Small and Medium Businesses</title>
<link rel="stylesheet" href="https://fonts.googleapis.com/css2?family=Open+Sans:wght@400;600;700;800&display=swap">
<style>
:root{
  --blue:#1a75bb;
  --blue-bright:#1f8ae0;
  --footer-blue:#0e72c2;
  --ink:#222;
  --text:#444;
  --muted:#777;
  --dark:#2b2b2b;
  --black:#111;
  --card:#f5f5f5;
  --card-line:#e6e6e6;
  --white:#fff;
}
*{box-sizing:border-box;margin:0;padding:0}
html,body{width:1200px;height:2419px;overflow:hidden;background:var(--white)}
body{font-family:"Open Sans",Arial,sans-serif;color:var(--text);position:relative}
.abs{position:absolute}

/* header */
.topline{left:0;top:0;width:1200px;height:5px;background:var(--dark)}
.site-header{left:0;top:5px;width:1200px;height:116px;background:var(--white)}
.brand{left:76px;top:30px;display:flex;align-items:center;gap:14px}
.brand-dot{width:40px;height:40px;border-radius:50%;background:var(--blue)}
.brand-name{font-size:34px;font-weight:700;color:var(--ink);letter-spacing:-0.5px}
.header-phone{right:73px;top:20px;display:flex;align-items:center;gap:12px;font-size:23px;font-weight:700;color:var(--blue)}
.phone-badge{width:36px;height:36px;border-radius:50%;background:#777;display:flex;align-items:center;justify-content:center}
.main-nav{right:73px;top:82px;display:flex;gap:46px;font-size:14.5px;font-weight:700;color:var(--ink);letter-spacing:.3px}
.main-nav .active{color:var(--blue)}

/* hero */
.hero{left:0;top:121px;width:1200px;height:553px;background:linear-gradient(90deg,#8e9aa6 0%,#b8c2cb 35%,#e4e2de 62%,#d9cdbf 80%,#c8c7c8 100%)}
.hero-caption{left:76px;top:318px;width:593px;height:163px;background:rgba(20,20,20,.82);padding:12px 22px}
.hero-caption h1{font-size:39px;font-weight:800;color:var(--white);letter-spacing:.5px;line-height:1.2}
.hero-caption h1 span{color:var(--blue-bright)}
.hero-caption p{font-size:20.5px;font-weight:700;color:var(--white);line-height:1.45;margin-top:6px}
.slider-dots{left:561px;top:626px;display:flex;gap:6px}
.slider-dots i{width:11px;height:11px;border-radius:50%;background:var(--white);display:block}
.slider-dots i.on{background:var(--blue-bright)}

/* services */
.section-title{width:1200px;left:0;text-align:center;font-size:26px;font-weight:700;color:var(--ink);letter-spacing:1px}
.service-card{top:776px;width:330px;height:332px;background:var(--card);border:1px solid var(--card-line);box-shadow:0 14px 12px -10px rgba(0,0,0,.18);padding:30px 26px 0 26px}
.card-head{display:flex;align-items:center;gap:34px;height:60px}
.card-head svg{width:58px;height:58px}
.card-head h2{font-size:23px;font-weight:700;color:var(--blue);letter-spacing:.5px}
.service-list{list-style:none;margin-top:22px}
.service-list li{font-size:14.5px;color:var(--text);line-height:29.5px;display:flex;align-items:center;gap:16px}
.service-list li svg{width:14px;height:11px;flex:none}
.btn{display:inline-block;background:var(--blue);color:var(--white);font-weight:700;letter-spacing:.3px}
.service-card .btn{margin-top:18px;font-size:12.5px;padding:10px 16px}

/* bands */
.band{left:0;width:1200px;height:362px;background:var(--dark)}
.band-photo{position:absolute;top:0;height:362px}
.band-one .band-photo{left:0;width:621px;clip-path:polygon(0 0,100% 0,94% 100%,0 100%);background:linear-gradient(120deg,#5d6a78 0%,#c9d3dc 45%,#eef1f3 70%,#9aa5ae 100%)}
.band-two .band-photo{left:573px;width:627px;clip-path:polygon(6% 0,100% 0,100% 100%,0 100%);background:linear-gradient(110deg,#e6e9ec 0%,#c4ccd2 40%,#8d98a2 70%,#d8dde1 100%)}
.band-copy{position:absolute;top:64px;width:525px}
.band-one .band-copy{left:640px}
.band-two .band-copy{left:76px}
.band-copy h2{font-size:25px;font-weight:700;color:var(--white);letter-spacing:.5px}
.band-copy p{font-size:14.5px;line-height:25.5px;color:#e5e5e5;margin-top:18px}
.band-copy .btn{margin-top:40px;font-size:14px;padding:14px 32px}

/* partners */
.partners{left:172px;top:1996px;width:856px;display:flex;justify-content:space-between;align-items:center}
.partner-badge{height:28px;border-radius:4px;background:#c9ced3}

/* footer */
.site-footer{left:0;top:2074px;width:1200px;height:283px;background:var(--footer-blue);color:var(--white)}
.footer-brand{left:76px;top:50px;display:flex;align-items:center;gap:12px}
.footer-brand .brand-dot{background:var(--white);width:32px;height:32px}
.footer-brand .brand-name{color:var(--white);font-size:27px}
.branch-list{left:76px;top:129px;font-size:13.5px;line-height:23px}
.branch-list div{display:flex}
.branch-list span{width:115px}
.footer-col h3{font-size:12.5px;font-weight:700;letter-spacing:.5px;margin-bottom:18px}
.sitemap{left:368px;top:48px}
.sitemap a{display:block;font-size:13.5px;line-height:31.5px;color:var(--white);text-decoration:none}
.blog{left:535px;top:48px}
.blog-item{display:flex;gap:24px;margin-bottom:28px}
.blog-thumb{width:78px;height:55px;background:linear-gradient(135deg,#dfe6ec,#9fb3c4)}
.blog-item h4{font-size:14px;font-weight:700}
.blog-item p{font-size:12.5px;line-height:21px;margin-top:2px}
.signup{left:884px;top:48px;width:243px}
.signup-field{width:243px;height:40px;background:var(--white);color:#777;font-size:13px;padding:11px 14px}
.signup .btn{background:var(--black);float:right;margin-top:14px;font-size:13px;padding:11px 16px}

.bottom-bar{left:0;top:2357px;width:1200px;height:62px;background:var(--black);color:#999}
.copyright{left:76px;top:24px;font-size:11px}
.social{left:952px;top:19px;display:flex;gap:18px;align-items:center}
.social i{display:block;width:20px;height:20px;border-radius:50%;background:var(--white)}
.social b{font-size:13px;font-weight:400;color:#ccc;margin-left:14px}
</style>
</head>
<body>

<div class="abs topline"></div>
<header class="abs site-header">
  <div class="abs brand"><span class="brand-dot"></span><span class="brand-name">Korvane IT</span></div>
  <div class="abs header-phone">
    <span class="phone-badge"><svg width="20" height="20" viewBox="0 0 24 24"><path fill="#fff" d="M6.6 10.8a15 15 0 0 0 6.6 6.6l2.2-2.2a1 1 0 0 1 1-.25 11.4 11.4 0 0 0 3.6.57 1 1 0 0 1 1 1V20a1 1 0 0 1-1 1A17 17 0 0 1 3 4a1 1 0 0 1 1-1h3.5a1 1 0 0 1 1 1c0 1.25.2 2.45.57 3.57a1 1 0 0 1-.25 1z"/></svg></span>
    555-014-2200
  </div>
  <nav class="abs main-nav"><span class="active">HOME</span><span>SERVICES</span><span>WHY KORVANE IT</span><span>CONTACT US</span></nav>
</header>

<section class="abs hero" role="img" aria-label="Photo of a smiling support agent wearing a headset in a busy office"></section>
<div class="abs hero-caption">
  <h1>WELCOME TO <span>KORVANE</span> IT</h1>
  <p>We are an IT support company that provides commercial IT support and services to small and medium sized business.</p>
</div>
<div class="abs slider-dots"><i class="on"></i><i></i><i></i><i></i><i></i></div>

<h2 class="abs section-title" style="top:720px">OUR SERVICES</h2>

<article class="abs service-card" style="left:74px">
  <div class="card-head">
    <svg viewBox="0 0 58 58"><g fill="#222"><ellipse cx="29" cy="11" rx="24" ry="8"/><path d="M5 17c0 4.5 10.7 8 24 8s24-3.5 24-8v9c0 4.5-10.7 8-24 8S5 30.5 5 26z"/><path d="M5 32c0 4.5 10.7 8 24 8s24-3.5 24-8v9c0 4.5-10.7 8-24 8S5 45.5 5 41z"/></g></svg>
    <h2>DATA</h2>
  </div>
  <ul class="service-list">
    <li><svg viewBox="0 0 14 11"><path d="M1 6l4 4 8-9" stroke="#1a75bb" stroke-width="2.4" fill="none"/></svg>Managed IT Services</li>
    <li><svg viewBox="0 0 14 11"><path d="M1 6l4 4 8-9" stroke="#1a75bb" stroke-width="2.4" fill="none"/></svg>IT Support &amp; Consulting</li>
    <li><svg viewBox="0 0 14 11"><path d="M1 6l4 4 8-9" stroke="#1a75bb" stroke-width="2.4" fill="none"/></svg>IT Helpdesk Services</li>
    <li><svg viewBox="0 0 14 11"><path d="M1 6l4 4 8-9" stroke="#1a75bb" stroke-width="2.4" fill="none"/></svg>Network Security</li>
    <li><svg viewBox="0 0 14 11"><path d="M1 6l4 4 8-9" stroke="#1a75bb" stroke-width="2.4" fill="none"/></svg>Data Backup &amp; Recovery</li>
  </ul>
  <span class="btn">READ MORE</span>
</article>

<article class="abs service-card" style="left:435px">
  <div class="card-head">
    <svg viewBox="0 0 58 58"><path fill="#222" d="M14 46a11 11 0 0 1-1-22 15 15 0 0 1 28-5 12 12 0 0 1 4 27z"/></svg>
    <h2>CLOUD</h2>
  </div>
  <ul class="service-list">
    <li><svg viewBox="0 0 14 11"><path d="M1 6l4 4 8-9" stroke="#1a75bb" stroke-width="2.4" fill="none"/></svg>Nimbo Suite Migrations</li>
    <li><svg viewBox="0 0 14 11"><path d="M1 6l4 4 8-9" stroke="#1a75bb" stroke-width="2.4" fill="none"/></svg>Skylar Cloud Management Services</li>
    <li><svg viewBox="0 0 14 11"><path d="M1 6l4 4 8-9" stroke="#1a75bb" stroke-width="2.4" fill="none"/></svg>Cloud Migration Services</li>
    <li><svg viewBox="0 0 14 11"><path d="M1 6l4 4 8-9" stroke="#1a75bb" stroke-width="2.4" fill="none"/></svg>Hosted Virtual Servers</li>
    <li><svg viewBox="0 0 14 11"><path d="M1 6l4 4 8-9" stroke="#1a75bb" stroke-width="2.4" fill="none"/></svg>Hosted Telephone Systems</li>
  </ul>
  <span class="btn">READ MORE</span>
</article>

<article class="abs service-card" style="left:797px">
  <div class="card-head">
    <svg viewBox="0 0 24 24"><path fill="#222" d="M6.6 10.8a15 15 0 0 0 6.6 6.6l2.2-2.2a1 1 0 0 1 1-.25 11.4 11.4 0 0 0 3.6.57 1 1 0 0 1 1 1V20a1 1 0 0 1-1 1A17 17 0 0 1 3 4a1 1 0 0 1 1-1h3.5a1 1 0 0 1 1 1c0 1.25.2 2.45.57 3.57a1 1 0 0 1-.25 1z"/></svg>
    <h2>VOICE</h2>
  </div>
  <ul class="service-list">
    <li><svg viewBox="0 0 14 11"><path d="M1 6l4 4 8-9" stroke="#1a75bb" stroke-width="2.4" fill="none"/></svg>Ostrin PBX Consulting</li>
    <li><svg viewBox="0 0 14 11"><path d="M1 6l4 4 8-9" stroke="#1a75bb" stroke-width="2.4" fill="none"/></svg>Business Telephone Systems</li>
    <li><svg viewBox="0 0 14 11"><path d="M1 6l4 4 8-9" stroke="#1a75bb" stroke-width="2.4" fill="none"/></svg>Multiple Office Phone Systems</li>
    <li><svg viewBox="0 0 14 11"><path d="M1 6l4 4 8-9" stroke="#1a75bb" stroke-width="2.4" fill="none"/></svg>Tellmar Telephone Systems</li>
    <li><svg viewBox="0 0 14 11"><path d="M1 6l4 4 8-9" stroke="#1a75bb" stroke-width="2.4" fill="none"/></svg>SIP Trunks</li>
  </ul>
  <span class="btn">READ MORE</span>
</article>

<section class="abs band band-one" style="top:1165px">
  <div class="band-photo" role="img" aria-label="Photo of a team of support staff with headsets working at computer desks"></div>
  <div class="band-copy">
    <h2>WELCOME TO OUR WEBSITE</h2>
    <p>Lorem ipsum dolor sit amet, consect- etuer adipiscing elit, sed diam nonummy nibh euismod tincidunt ut laoreet dolore magna aliquam erat volutpat. Ut wisi enim ad minim veniam, quis nostrud exerci tation ullam.</p>
    <span class="btn">READ MORE</span>
  </div>
</section>

<section class="abs band band-two" style="top:1526px">
  <div class="band-photo" role="img" aria-label="Photo of a presenter holding a sign in front of a seated team in a bright meeting room"></div>
  <div class="band-copy">
    <h2>WHY KORVANE IT</h2>
    <p>Lorem ipsum dolor sit amet, consect- etuer adipiscing elit, sed diam nonummy nibh euismod tincidunt ut laoreet dolore magna aliquam erat volutpat. Ut wisi enim ad minim veniam, quis nostrud exerci tation ullam.</p>
    <span class="btn">READ MORE</span>
  </div>
</section>

<h2 class="abs section-title" style="top:1933px">OUR PARTNERS</h2>
<div class="abs partners" aria-label="Partner badges">
  <span class="partner-badge" style="width:86px"></span>
  <span class="partner-badge" style="width:74px"></span>
  <span class="partner-badge" style="width:78px"></span>
  <span class="partner-badge" style="width:50px"></span>
  <span class="partner-badge" style="width:100px"></span>
  <span class="partner-badge" style="width:66px"></span>
  <span class="partner-badge" style="width:110px"></span>
  <span class="partner-badge" style="width:22px"></span>
  <span class="partner-badge" style="width:52px"></span>
</div>

<footer class="abs site-footer">
  <div class="abs footer-brand"><span class="brand-dot"></span><span class="brand-name">Korvane IT</span></div>
  <div class="abs branch-list">
    <div><span>Main Number:</span>555-014-2200</div>
    <div><span>Houston:</span>555-014-3300</div>
    <div><span>San Antonio:</span>555-014-4400</div>
    <div><span>Austin:</span>555-014-5500</div>
    <div><span>Tulsa:</span>555-014-6600</div>
    <div><span>Oklahoma City:</span>555-014-7700</div>
  </div>
  <div class="abs footer-col sitemap">
    <h3>SITE MAP</h3>
    <a>Home</a><a>Services</a><a>Why Korvane IT</a><a>Contact us</a>
  </div>
  <div class="abs footer-col blog">
    <h3>BLOG POSTS</h3>
    <div class="blog-item"><div class="blog-thumb" role="img" aria-label="Blog post thumbnail photo"></div><div><h4>Consectetuer adipiscing elit</h4><p>Aenean a nibh eget turpis<br>vehicula tempus ac...</p></div></div>
    <div class="blog-item"><div class="blog-thumb" role="img" aria-label="Blog post thumbnail photo"></div><div><h4>Consectetuer adipiscing elit</h4><p>Aenean a nibh eget turpis<br>vehicula tempus ac...</p></div></div>
  </div>
  <div class="abs footer-col signup">
    <h3>EMAIL SIGN UP</h3>
    <div class="signup-field">Enter Email Address</div>
    <span class="btn">SIGN UP</span>
  </div>
</footer>

<div class="abs bottom-bar">
  <div class="abs copyright">Copyright © 2017. Company Name. All Right Reserved</div>
  <div class="abs social"><i></i><i></i><i></i><i></i><i></i><b>X10</b></div>
</div>

</body>
</html>
```